依頼詳細
8月の19日に宮城県南三陸町の、つばさ交流センターというところで公演を予定しています。
公演に際して、町民の方々に配布するチラシの作成を依頼させて頂きたいです。

ターゲットは、未就学児くらいの子供とその親や、高齢者の方を想定しています。

当日は公演本編の他に、お客様と出演者の交流会(お茶っこ)や、
子供たちと遊ぶ時間も設ける予定です。

明るくポップで、楽しいごきげんなイメージが伝わるようなデザインを希望します。
記載項目
【表面】

■タイトル

■場所

■入場料

■問い合わせ

■主催/協力

【裏面】

■あらすじ

■キャスト

■スタッフ

■団体紹介

サイズ
A4
ページ数
両面
希望イメージ
シンプル 複雑
単色 カラフル
暗い 明るい
日常 高級
遊び心 厳粛
未来的 伝統的
女性的 男性的
希望する色
黄・オレンジ系、ロゴマークとも調和がとれると嬉しいです。
納品ファイル
• 高解像度JPG (.jpg)
• イラストレーター形式 (.ai)
• PNG形式 (.png)
補足説明
・PDFファイルでも納品いただきたいです。
・裏面のキャストは顔写真を入れていただきたいです。データは後程お渡しします。
・7月3日までに最終データを受け取れるととても助かります!
■ 選んだ理由

民話の内容に沿ったオリジナルのイラストと、お茶っこやモロッパなど細かいところにも
こだわりをもって丁寧に作ってくださっている印象で、メンバー内で一番人気で選ばせていただきました!

■ 提案者全員のお礼・コメント

民話の内容に興味をもって作ってくださったり、お子さんやお年寄りにも見やすいように。と
工夫をしてくださったりして、どれも思いが伝わってきて嬉しくなりました!
これまでは自分たちでチラシの作成もしていたので、プロフェッショナルの手にかかると
こんな風に世界が広がるんだなと、とてもクリエイティブな部分でも刺激を受けました。
ありがとうございました!!

```html
<!DOCTYPE html>
<html lang="ja">
<head>
<meta charset="utf-8">
<title>にこにこ一座2023 南三陸公演「ばば山」</title>
<link rel="stylesheet" href="https://fonts.googleapis.com/css2?family=M+PLUS+Rounded+1c:wght@500;800&family=Kosugi+Maru&display=swap">
<style>
  :root {
    --paper: #fdf7e6;
    --ink: #2a2f4a;
    --navy: #253154;
    --pink: #f7b9cb;
    --yellow: #fbe27c;
    --blue: #bfe1f0;
    --orange: #f8c27f;
    --lilac: #d9c7ec;
    --green: #cde59e;
    --teal: #3aa79a;
    --accent: #e8604c;
    --white: #ffffff;
  }
  html, body { margin: 0; padding: 0; overflow: hidden; }
  body { width: 849px; height: 1200px; background: var(--paper); }
  .flyer {
    position: relative; width: 849px; height: 1200px; overflow: hidden;
    background: var(--paper); color: var(--ink);
    font-family: "M PLUS Rounded 1c", "Kosugi Maru", sans-serif;
  }
  .blobs { position: absolute; inset: 0; }
  .block { position: absolute; left: 0; width: 100%; text-align: center; margin: 0; }
  .event-label { top: 30px; font-size: 42px; font-weight: 800; letter-spacing: 2px; }
  .event-label span { margin-left: 28px; }
  .title { top: 140px; font-size: 150px; font-weight: 800; letter-spacing: 4px; line-height: 1; }
  .subtitle { top: 345px; font-size: 32px; font-weight: 800; }
  .date { top: 425px; font-size: 66px; font-weight: 800; }
  .date .small { font-size: 46px; }
  .date .weekday {
    display: inline-block; width: 70px; height: 70px; line-height: 70px;
    border-radius: 50%; background: var(--navy); color: var(--white);
    font-size: 44px; vertical-align: 6px; margin-left: 6px;
  }
  .time { top: 528px; left: 90px; text-align: left; font-size: 40px; font-weight: 800; }
  .time small { font-size: 24px; font-weight: 500; }
  .venue { top: 588px; left: 90px; text-align: left; font-size: 34px; font-weight: 800; }
  .venue small { display: block; font-size: 22px; font-weight: 500; margin-top: 6px; }
  .admission {
    position: absolute; left: 42px; top: 745px; width: 242px; padding: 22px 0;
    background: var(--teal); color: var(--white); border-radius: 18px;
    text-align: center; font-weight: 800;
  }
  .admission p { margin: 0; font-size: 38px; line-height: 1.35; }
  .admission .note {
    display: inline-block; margin-top: 10px; padding: 2px 14px;
    background: var(--white); color: var(--teal); border-radius: 10px; font-size: 24px;
  }
  .group-mark {
    position: absolute; left: 500px; top: 770px; width: 290px; height: 260px;
    display: flex; flex-direction: column; align-items: center; justify-content: center; gap: 18px;
  }
  .group-mark .dot { width: 120px; height: 120px; border-radius: 50%; background: var(--accent); }
  .group-mark .name { font-size: 40px; font-weight: 800; color: var(--ink); }
  .notes { position: absolute; left: 38px; top: 1000px; margin: 0; padding: 0; list-style: none; font-size: 22px; font-weight: 800; line-height: 1.6; }
  .notes li::before { content: "★ "; }
  .contact {
    position: absolute; left: 0; bottom: 0; width: 100%; height: 110px;
    background: var(--navy); color: var(--white); box-sizing: border-box; padding: 12px 38px;
  }
  .contact h2 { margin: 0; font-size: 22px; font-weight: 800; }
  .contact .row { display: flex; justify-content: space-between; align-items: flex-end; margin-top: 6px; }
  .contact .item { display: flex; align-items: center; gap: 10px; font-size: 30px; font-weight: 800; }
  .contact .item label { display: block; font-size: 14px; font-weight: 500; }
  .contact svg { width: 34px; height: 34px; }
</style>
</head>
<body>
<main class="flyer">
  <svg class="blobs" viewBox="0 0 849 1200" aria-hidden="true">
    <path d="M-40 60 C 60 -30, 260 20, 250 170 C 240 300, 90 330, 10 300 C -60 270, -80 140, -40 60 Z" fill="var(--pink)"/>
    <path d="M280 120 C 400 60, 620 90, 640 200 C 660 320, 470 360, 360 330 C 240 300, 170 180, 280 120 Z" fill="var(--yellow)"/>
    <path d="M620 40 C 740 -10, 900 60, 880 190 C 860 300, 740 330, 660 270 C 580 210, 540 80, 620 40 Z" fill="var(--blue)"/>
    <path d="M-30 420 C 80 380, 210 440, 200 560 C 190 660, 60 700, -20 650 Z" fill="var(--orange)"/>
    <path d="M620 400 C 740 360, 880 420, 870 560 C 860 660, 740 680, 660 620 C 580 560, 540 440, 620 400 Z" fill="var(--lilac)"/>
    <path d="M440 720 C 560 650, 820 660, 860 800 C 900 960, 760 1080, 600 1070 C 450 1060, 360 800, 440 720 Z" fill="var(--green)"/>
    <path d="M-20 730 C 100 690, 330 700, 330 830 C 330 960, 140 990, 20 960 C -60 940, -80 770, -20 730 Z" fill="var(--yellow)"/>
  </svg>

  <p class="block event-label">にこにこ一座2023<span>南三陸公演</span></p>
  <h1 class="block title">「ばば山」</h1>
  <p class="block subtitle">〜民話を基にアレンジした創作演劇作品〜</p>
  <p class="block date">2023<span class="small">年</span>8<span class="small">月</span>19<span class="small">日</span><span class="weekday">土</span></p>
  <p class="block time">開演 14:00 <small>(開場 13:30 / 終演予定 15:00)</small></p>
  <p class="block venue">場所　南三陸町つばさ交流センター 第2研修室
    <small>(〒986-0000 宮城県本吉郡南三陸町志津川緑ヶ丘12-3)</small></p>

  <section class="admission">
    <p>入場無料！</p>
    <p>予約不要！</p>
    <span class="note">当日参加OK</span>
  </section>

  <div class="group-mark">
    <span class="dot"></span>
    <span class="name">にこにこ一座</span>
  </div>

  <ul class="notes">
    <li>終演後、お茶っこ(交流会)を予定しています</li>
    <li>モロッパもあるよ！</li>
  </ul>

  <footer class="contact">
    <h2>■お問い合わせ</h2>
    <div class="row">
      <div class="item">
        <svg viewBox="0 0 24 24" aria-hidden="true"><rect x="2" y="5" width="20" height="14" rx="2" fill="var(--white)"/><path d="M3 6 L12 13 L21 6" stroke="var(--navy)" stroke-width="2" fill="none"/></svg>
        <div><label>メール</label>nikoniko-za@example.com</div>
      </div>
      <div class="item">
        <svg viewBox="0 0 24 24" aria-hidden="true"><path d="M6.6 10.8a15 15 0 0 0 6.6 6.6l2.2-2.2a1 1 0 0 1 1-.25 11.4 11.4 0 0 0 3.6.57 1 1 0 0 1 1 1V20a1 1 0 0 1-1 1A17 17 0 0 1 3 4a1 1 0 0 1 1-1h3.5a1 1 0 0 1 1 1c0 1.25.2 2.45.57 3.6a1 1 0 0 1-.25 1z" fill="var(--white)"/></svg>
        <div><label>TEL</label>050-0000-1234</div>
      </div>
    </div>
  </footer>
</main>
</body>
</html>
```